Australian Software Consultancy needs new Business Card Design

Design Business Card based on existing design artefacts (attached). We are open to all designs. As its a 2 sided design and we thought it might be quite striking to have one side with a black background and te other side with a white background.

Target Market(s)

Financial Services mainly.

Industry/Entity Type

Business

Contact Information for Business Card

Name :
Position :
Email :

Requirements
Must have
• Funky design using our existing assets

```html
<!DOCTYPE html>
<html lang="en">
<head>
<meta charset="utf-8">
<title>Clear Logic Business Card</title>
<link href="https://fonts.googleapis.com/css2?family=Montserrat:wght@600;700&family=Open+Sans:wght@400;600&display=swap" rel="stylesheet">
<style>
  :root {
    --backdrop: #e9e7e5;
    --card-white: #f4f4f4;
    --card-black: #1c1a1a;
    --red: #d71920;
    --ink: #222222;
    --ink-soft: #555555;
    --white: #ffffff;
  }
  * { margin: 0; padding: 0; box-sizing: border-box; }
  html, body { width: 1200px; height: 890px; overflow: hidden; }
  body {
    background: var(--backdrop);
    font-family: "Open Sans", Arial, sans-serif;
    position: relative;
  }
  .card {
    position: absolute;
    width: 525px;
    height: 300px;
    overflow: hidden;
    box-shadow: 0 6px 18px rgba(0,0,0,.18);
  }
  .card--front { left: 45px; top: 295px; background: var(--card-white); }
  .card--back  { left: 630px; top: 295px; background: var(--card-black); }

  .wordmark {
    font-family: "Montserrat", Arial, sans-serif;
    font-weight: 700;
    letter-spacing: 1px;
    text-transform: uppercase;
    white-space: nowrap;
  }
  .card--front .wordmark {
    position: absolute; left: 44px; top: 38px;
    font-size: 21px; color: var(--ink);
  }
  .card--back .wordmark {
    position: absolute; left: 268px; top: 132px;
    font-size: 31px; color: var(--white);
  }

  .name-marker {
    position: absolute; left: 0; top: 86px;
    width: 30px; height: 22px; background: var(--red);
  }
  .person { position: absolute; left: 44px; top: 84px; }
  .person__name {
    font-family: "Montserrat", Arial, sans-serif;
    font-weight: 600; font-size: 14px; color: var(--ink);
    text-transform: uppercase; letter-spacing: .5px;
  }
  .person__name .accent { color: var(--red); }
  .person__title { font-size: 11px; color: var(--ink-soft); margin-top: 1px; }

  .contacts {
    position: absolute; left: 44px; top: 156px;
    list-style: none;
  }
  .contacts li {
    display: flex; align-items: center; gap: 10px;
    font-size: 13px; color: var(--ink); line-height: 24px;
  }
  .contacts svg { width: 13px; height: 13px; flex: none; }

  .edge-band {
    position: absolute; left: 0; bottom: 0;
    width: 300px; height: 9px; background: var(--red);
  }
  .edge-band--side {
    position: absolute; left: 0; top: 108px;
    width: 4px; height: 192px; background: var(--red);
  }
  .accent-circle { position: absolute; }
  .card--front .accent-circle { right: -70px; bottom: -95px; }
  .card--back .accent-circle { left: -95px; top: -20px; }
</style>
</head>
<body>

<section class="card card--front" aria-label="Business card, front">
  <div class="wordmark">Clear Logic</div>

  <span class="name-marker"></span>
  <div class="person">
    <div class="person__name">Your <span class="accent">Name</span></div>
    <div class="person__title">Job Title</div>
  </div>

  <ul class="contacts">
    <li>
      <svg viewBox="0 0 16 16"><circle cx="8" cy="8" r="8" fill="#d71920"/><path d="M5 4.5l2 2-1 1c.6 1.2 1.3 1.9 2.5 2.5l1-1 2 2-1.3 1.3C7.5 12 4 8.5 3.7 5.8z" fill="#fff"/></svg>
      000-111-222-44
    </li>
    <li>
      <svg viewBox="0 0 16 16"><rect x="0" y="3" width="16" height="11" fill="#d71920"/><path d="M0 3l8 6 8-6" fill="none" stroke="#fff" stroke-width="1.4"/></svg>
      yourmail@email.com
    </li>
    <li>
      <svg viewBox="0 0 16 16"><circle cx="8" cy="8" r="8" fill="#d71920"/><circle cx="8" cy="8" r="4.5" fill="none" stroke="#fff" stroke-width="1.2"/><path d="M3.5 8h9M8 3.5v9" stroke="#fff" stroke-width="1"/></svg>
      www.clear-logic.com
    </li>
  </ul>

  <span class="edge-band--side"></span>
  <span class="edge-band"></span>

  <svg class="accent-circle" width="280" height="280" viewBox="0 0 280 280" aria-hidden="true">
    <circle cx="140" cy="140" r="128" fill="none" stroke="#d71920" stroke-width="16"/>
  </svg>
</section>

<section class="card card--back" aria-label="Business card, back">
  <svg class="accent-circle" width="340" height="340" viewBox="0 0 340 340" aria-hidden="true">
    <circle cx="170" cy="170" r="155" fill="none" stroke="#d71920" stroke-width="20"/>
  </svg>
  <div class="wordmark">Clear Logic</div>
</section>

</body>
</html>
```